Fernwick Ridge Glide Treks

We offer guided cross country ( Nordic ) skiing tours in the National Forest bordering Yellowstone National Park. I need a website that attracts individuals by using photos ( provided by me ) , brief descriptions of what to expect, a place with phone numbers to call for a tour, and I would like the website to feature the same color scheme as the logo, which I will upload.

```html
<!DOCTYPE html>
<html lang="en">
<head>
<meta charset="utf-8">
<title>Fernwick Ridge Glide Treks</title>
<link href="https://fonts.googleapis.com/css2?family=Nunito+Sans:wght@400;600;700;800;900&display=swap" rel="stylesheet">
<style>
:root{
  --blue:#5f81c9;
  --blue-deep:#4f6fb5;
  --slate:#433f43;
  --ink:#1f1f22;
  --text:#333;
  --white:#fff;
  --footer:#1b1b1e;
  --nav:#444;
}
*{box-sizing:border-box;margin:0;padding:0}
html,body{width:1200px;height:4124px;overflow:hidden;background:var(--white)}
body{font-family:"Nunito Sans",Arial,sans-serif;color:var(--text)}
.page{position:relative;width:1200px;height:4124px;overflow:hidden}
.abs{position:absolute}
.btn{position:absolute;display:flex;align-items:center;justify-content:center;border-radius:22px;font-weight:800;font-size:14px;letter-spacing:.2px;text-transform:uppercase;white-space:nowrap}
.btn--blue{background:var(--blue);color:var(--white)}
.btn--white{background:var(--white);color:var(--blue)}

/* header */
.site-header{left:0;top:0;width:1200px;height:80px;background:var(--white);z-index:3}
.brand{left:70px;top:-6px;width:130px;height:130px;border-radius:50%;background:var(--white);border:3px solid var(--ink);z-index:5;display:flex;align-items:center;justify-content:center;text-align:center;font-weight:800;font-size:14px;line-height:1.15;color:var(--blue-deep);padding:14px}
.nav{position:absolute;left:0;top:0;width:1200px;height:80px;z-index:4}
.nav-link{position:absolute;top:29px;font-size:15px;line-height:20px;text-transform:uppercase;color:var(--nav);letter-spacing:.3px;white-space:nowrap}
.nav-link--active{color:var(--blue)}
.nav-call{top:18px;height:42px;font-size:13px}

/* hero */
.hero{left:0;top:80px;width:1200px;height:557px;background:linear-gradient(160deg,#c7d3ec 0%,#e6e8ee 35%,#d3d4d8 60%,#f1f1f3 85%,#c9c9cd 100%)}
.hero-title{left:100px;top:237px;width:1000px;text-align:center;font-size:44px;font-weight:900;line-height:60px;color:var(--white);text-transform:uppercase;text-shadow:-2px -2px 0 #222,2px -2px 0 #222,-2px 2px 0 #222,2px 2px 0 #222,0 3px 6px rgba(0,0,0,.4)}

/* about */
.about-photo{left:72px;top:668px;width:518px;height:393px;border:2px solid var(--ink);background:linear-gradient(180deg,#8aa2ad 0%,#a4a89a 40%,#e2a35f 55%,#c9c8cc 75%,#3b3a3c 100%)}
.about-title{left:610px;top:692px;font-size:31px;font-weight:900;color:var(--ink);text-transform:uppercase}
.about-text{left:610px;top:743px;width:515px;font-size:18px;line-height:29.3px;color:var(--text)}

/* offers */
.offer-band{left:0;top:1094px;width:1200px;height:80px;background:var(--blue);display:flex;align-items:center;justify-content:center;color:var(--white);font-size:30px;font-weight:900;text-transform:uppercase}
.offer-row{left:0;width:1200px;height:461px}
.offer-title{width:300px;text-align:center;color:var(--white);font-size:32px;font-weight:900;line-height:45px;text-transform:uppercase}

/* testimonial */
.section-title{left:0;width:1200px;text-align:center;font-size:30px;font-weight:900;color:var(--ink);text-transform:uppercase}
.quote-text{left:215px;top:3316px;width:770px;text-align:center;font-size:18px;line-height:29px}
.quote-name{left:0;top:3427px;width:1200px;text-align:center;font-size:17px;line-height:24px}

/* call band */
.call-band{left:0;top:3508px;width:1200px;height:320px;background:var(--blue)}
.call-title{left:0;top:3584px;width:1200px;text-align:center;color:var(--white);font-size:31px;font-weight:900;text-transform:uppercase}
.call-text{left:0;top:3637px;width:1200px;text-align:center;color:var(--white);font-size:19px}

/* footer */
.footer-brand{left:72px;top:3826px;width:82px;height:82px;border-radius:50%;background:var(--white);display:flex;align-items:center;justify-content:center;text-align:center;font-size:9.5px;font-weight:800;line-height:1.15;color:var(--blue-deep);padding:8px}
.footer-text{left:72px;top:3924px;width:320px;color:var(--white);font-size:15px;line-height:23px}
.footer-head{top:3832px;color:var(--white);font-size:19px;font-weight:400}
.footer-list{list-style:none;color:var(--white);font-size:15px;line-height:28px}
.footer-list li::before{content:"• ";}
.social{top:3897px;width:29px;height:29px;border-radius:50%;background:var(--white)}
.copyright{left:0;top:4040px;width:1200px;text-align:center;color:var(--white);font-size:15px}
.copyright span{color:var(--blue)}
</style>
</head>
<body>
<div class="page">

  <!-- header -->
  <header class="abs site-header"></header>
  <div class="abs brand">Fernwick Ridge Glide Treks</div>
  <nav class="nav">
    <span class="nav-link nav-link--active" style="left:543px">Home</span>
    <span class="nav-link" style="left:641px">About</span>
    <span class="nav-link" style="left:746px">What We Offer</span>
    <span class="btn btn--blue nav-call" style="left:904px;width:223px">Call Us Now :555-014-2270</span>
  </nav>

  <!-- hero -->
  <section class="abs hero" role="img" aria-label="Illustration of a Nordic skier silhouette gliding past snowy trees and mountains"></section>
  <h1 class="abs hero-title">Skiing tours in the<br>National Forest boarding<br>Yellowstone National Park.</h1>
  <span class="btn btn--blue" style="left:530px;top:440px;width:140px;height:40px">Call a Tour</span>

  <!-- about -->
  <div class="abs about-photo" role="img" aria-label="Photo of a snowy mountain peak lit by evening sun"></div>
  <h2 class="abs about-title">About Us</h2>
  <p class="abs about-text">Lorem Ipsum is simply dummy text of the printing and typesetting industry. Lorem Ipsum has been the industry's standard dummy text ever since the 1500s, when an unknown printer took a galley of type and scrambled it to make a type specimen book. It has survived not only five centuries, but also the leap into electronic typesetting, remaining essentially unchanged. It was popularised in the 1960s with the release of Letraset sheets containing Lorem Ipsum passages,</p>
  <span class="btn btn--blue" style="left:613px;top:1000px;width:140px;height:40px">Read More</span>

  <!-- offers -->
  <div class="abs offer-band">What We Offer</div>

  <svg class="abs offer-row" style="top:1174px" viewBox="0 0 1200 461" role="img" aria-label="Photo of a skier on a snowy forest trail">
    <defs><linearGradient id="g1" x1="0" y1="0" x2="1" y2="1"><stop offset="0" stop-color="#6b6e72"/><stop offset=".45" stop-color="#e9ebee"/><stop offset="1" stop-color="#f6f6f8"/></linearGradient></defs>
    <rect width="1200" height="461" fill="url(#g1)"/>
    <rect x="900" width="300" height="461" fill="#fff"/>
    <circle cx="905" cy="230" r="268" fill="#fff"/>
    <circle cx="918" cy="229" r="210" fill="#5f81c9" stroke="#1f1f22" stroke-width="3"/>
    <circle cx="684" cy="205" r="46" fill="#f3f5fa" stroke="#1f1f22" stroke-width="3"/>
  </svg>
  <div class="abs offer-title" style="left:768px;top:1343px">Bear Creek -<br>Upper</div>
  <span class="btn btn--white" style="left:852px;top:1474px;width:140px;height:40px">Call a Tour</span>

  <svg class="abs offer-row" style="top:1658px" viewBox="0 0 1200 461" role="img" aria-label="Photo of a snow covered mountain under a blue sky">
    <defs><linearGradient id="g2" x1="0" y1="0" x2="0" y2="1"><stop offset="0" stop-color="#2d5aa5"/><stop offset=".45" stop-color="#7da0d3"/><stop offset=".6" stop-color="#e8ecf2"/><stop offset="1" stop-color="#3a3f47"/></linearGradient></defs>
    <rect width="1200" height="461" fill="url(#g2)"/>
    <rect width="300" height="461" fill="#fff"/>
    <circle cx="295" cy="230" r="268" fill="#fff"/>
    <circle cx="290" cy="230" r="210" fill="#433f43" stroke="#5f81c9" stroke-width="4"/>
    <circle cx="508" cy="224" r="46" fill="#f3f5fa" stroke="#1f1f22" stroke-width="3"/>
  </svg>
  <div class="abs offer-title" style="left:136px;top:1827px">Electric<br>Peak 2</div>
  <span class="btn btn--blue" style="left:225px;top:1958px;width:140px;height:40px">Call a Tour</span>

  <svg class="abs offer-row" style="top:2147px" viewBox="0 0 1200 461" role="img" aria-label="Photo of snowy pine trees under a grey winter sky">
    <defs><linearGradient id="g3" x1="0" y1="0" x2="0" y2="1"><stop offset="0" stop-color="#aeb3b8"/><stop offset=".5" stop-color="#4d5358"/><stop offset=".75" stop-color="#cfd2d6"/><stop offset="1" stop-color="#eef0f2"/></linearGradient></defs>
    <rect width="1200" height="461" fill="url(#g3)"/>
    <rect x="900" width="300" height="461" fill="#fff"/>
    <circle cx="905" cy="230" r="268" fill="#fff"/>
    <circle cx="918" cy="229" r="210" fill="#5f81c9" stroke="#1f1f22" stroke-width="3"/>
    <circle cx="684" cy="235" r="46" fill="#f3f5fa" stroke="#1f1f22" stroke-width="3"/>
  </svg>
  <div class="abs offer-title" style="left:763px;top:2316px">Mineral<br>Hil</div>
  <span class="btn btn--white" style="left:852px;top:2446px;width:140px;height:40px">Call a Tour</span>

  <svg class="abs offer-row" style="top:2634px" viewBox="0 0 1200 461" role="img" aria-label="Photo of dark evergreen forest in drifting mist">
    <defs><linearGradient id="g4" x1="0" y1="0" x2="1" y2="0"><stop offset="0" stop-color="#2a2d31"/><stop offset=".55" stop-color="#b9bcc0"/><stop offset="1" stop-color="#25282c"/></linearGradient></defs>
    <rect width="1200" height="461" fill="url(#g4)"/>
    <rect width="300" height="461" fill="#fff"/>
    <circle cx="295" cy="230" r="268" fill="#fff"/>
    <circle cx="290" cy="230" r="210" fill="#433f43" stroke="#5f81c9" stroke-width="4"/>
    <circle cx="512" cy="230" r="46" fill="#f3f5fa" stroke="#1f1f22" stroke-width="3"/>
  </svg>
  <div class="abs offer-title" style="left:136px;top:2803px">Snow and<br>Trees</div>
  <span class="btn btn--blue" style="left:225px;top:2934px;width:140px;height:40px">Call a Tour</span>

  <!-- testimonial -->
  <h2 class="abs section-title" style="top:3136px">Testimonial</h2>
  <div class="abs" role="img" aria-label="Portrait of the reviewer" style="left:557px;top:3191px;width:86px;height:86px;border-radius:50%;border:3px solid #e2e2e2;background:linear-gradient(180deg,#cfe4ef,#e9a08c)"></div>
  <div class="abs" style="left:0;top:3282px;width:1200px;text-align:center;color:var(--blue);font-size:34px;font-weight:900;line-height:34px">&ldquo;</div>
  <svg class="abs" style="left:72px;top:3284px" width="24" height="34" viewBox="0 0 24 34" aria-label="Previous"><path d="M18 3 L5 17 L18 31" fill="none" stroke="#5f81c9" stroke-width="4" stroke-linecap="round"/></svg>
  <svg class="abs" style="left:1102px;top:3284px" width="24" height="34" viewBox="0 0 24 34" aria-label="Next"><path d="M6 3 L19 17 L6 31" fill="none" stroke="#5f81c9" stroke-width="4" stroke-linecap="round"/></svg>
  <p class="abs quote-text">There are many variations of passages of Lorem Ipsum available, but the majority have suffered alteration in some form, by injected humour, or randomised words which don't look even slightly believable.</p>
  <p class="abs quote-name">– JOHN DOE<br>Businessman</p>

  <!-- call to action -->
  <section class="abs call-band"></section>
  <h2 class="abs call-title">Call Us Now</h2>
  <p class="abs call-text">It is a long established fact that a reader will be distracted</p>
  <span class="btn btn--white" style="left:530px;top:3690px;width:140px;height:40px">Call Us Now</span>

  <!-- footer -->
  <svg class="abs" style="left:0;top:3740px" width="1200" height="384" viewBox="0 0 1200 384">
    <path d="M0 42 C200 60 420 40 650 30 C880 20 1050 10 1200 0 L1200 384 L0 384 Z" fill="#1b1b1e"/>
  </svg>
  <div class="abs footer-brand">Fernwick Ridge Glide Treks</div>
  <p class="abs footer-text">It is a long established fact that a reader will be distracted by the readable content</p>

  <h3 class="abs footer-head" style="left:482px">Quick Link</h3>
  <ul class="abs footer-list" style="left:486px;top:3892px">
    <li>Home</li><li>About</li><li>What We Offer</li>
  </ul>
  <h3 class="abs footer-head" style="left:723px">Offer</h3>
  <ul class="abs footer-list" style="left:727px;top:3892px">
    <li>Castle</li><li>Mineral Hil</li><li>More snow and trees</li>
  </ul>
  <h3 class="abs footer-head" style="left:969px">Follow Us :</h3>
  <span class="abs social" style="left:970px" aria-label="Social profile"></span>
  <span class="abs social" style="left:1005px" aria-label="Social profile"></span>
  <span class="abs social" style="left:1040px" aria-label="Social profile"></span>
  <span class="abs social" style="left:1075px" aria-label="Social profile"></span>

  <p class="abs copyright">Copyright <span>Fernwick Ridge Glide Treks</span> 2021 . All rights reserved.</p>
</div>
</body>
</html>
```